80's Band Poster

I'm looking for help. My wife's name is Marisol and both my and my son's name are Theo. She signs all our mail with "Marisol and the Theos." I think it would be an amazing Christmas present to get an 80's themed band poster for her as if she was the lead singer of the band Marisol and the Theos. Lots of angular pinks and teals? Maybe just a logo/design. I don't know. I'd love to see some ideas. Let me know if you have any questions. I can provide pictures if you think you's like to include them in your design/illustration.

Requirements
Must have
• Fun. Excitement. 80's

```html
<!DOCTYPE html>
<html lang="en">
<head>
<meta charset="utf-8">
<title>Marisol and the Theos</title>
<link rel="stylesheet" href="https://fonts.googleapis.com/css2?family=Righteous&display=swap">
<style>
  :root {
    --magenta: #d93690;
    --magenta-deep: #b8277a;
    --hot-pink: #f2399c;
    --pink-soft: #f77cc0;
    --teal: #2f7d98;
    --teal-deep: #21647d;
    --sky: #56b6e8;
    --lilac: #b866c4;
    --ink: #1c1a1c;
    --white: #ffffff;
  }
  html, body {
    margin: 0;
    padding: 0;
    overflow: hidden;
    background: var(--white);
  }
  .poster {
    position: relative;
    width: 839px;
    height: 1200px;
    overflow: hidden;
  }
  .backdrop {
    position: absolute;
    inset: 0;
    background: linear-gradient(90deg,
      var(--magenta-deep) 0%,
      var(--magenta) 30%,
      var(--hot-pink) 52%,
      var(--lilac) 60%,
      var(--teal) 70%,
      var(--teal-deep) 100%);
  }
  .backdrop-wash {
    position: absolute;
    left: 400px;
    top: 560px;
    width: 220px;
    height: 640px;
    background: linear-gradient(180deg, rgba(86,182,232,0) 0%, var(--sky) 45%, var(--sky) 100%);
  }
  .backdrop-fade {
    position: absolute;
    left: 0;
    bottom: 0;
    width: 420px;
    height: 420px;
    background: linear-gradient(180deg, rgba(247,124,192,0) 0%, var(--pink-soft) 100%);
  }
  .artwork {
    position: absolute;
    inset: 0;
  }
  .band-title {
    font-family: "Righteous", sans-serif;
    text-anchor: middle;
  }
</style>
</head>
<body>
<main class="poster">
  <div class="backdrop" role="img" aria-label="Distressed pink and teal background with faint folk-style pattern"></div>
  <div class="backdrop-wash"></div>
  <div class="backdrop-fade"></div>

  <svg class="artwork" viewBox="0 0 839 1200" width="839" height="1200">
    <circle class="sun-ring" cx="437" cy="541" r="346" fill="none" stroke="var(--white)" stroke-width="44"/>
    <circle class="sun-core" cx="437" cy="541" r="285" fill="var(--hot-pink)" role="img" aria-label="Pink disc with white ornamental pattern"/>

    <g class="floor-bands" fill="var(--pink-soft)">
      <polygon points="160,1010 245,1060 70,1200 0,1200 0,1110"/>
      <polygon points="345,1100 420,1130 330,1200 230,1200"/>
    </g>

    <g class="stripes" fill="none" stroke="var(--ink)" stroke-width="16" stroke-linejoin="miter">
      <polyline points="298,0 298,330"/>
      <polyline points="345,0 345,330"/>
      <polyline points="384,0 384,330"/>
      <polyline points="160,670 160,1010 0,1110"/>
      <polyline points="245,690 245,1060 70,1200"/>
      <polyline points="345,670 345,1100 230,1200"/>
      <polyline points="420,760 420,1130 330,1200"/>
      <polyline points="515,670 515,1170 490,1200"/>
      <polyline points="600,670 600,1140 560,1200"/>
    </g>

    <g class="band-title">
      <text class="title-lead" x="437" y="440" font-size="104" textLength="480" lengthAdjust="spacingAndGlyphs" fill="var(--teal-deep)">MARISOL</text>
      <text class="title-join" x="437" y="520" font-size="56" textLength="260" lengthAdjust="spacingAndGlyphs" fill="var(--ink)">AND THE</text>
      <text class="title-tail" x="437" y="630" font-size="116" textLength="430" lengthAdjust="spacingAndGlyphs" fill="var(--white)">THEOS</text>
    </g>
  </svg>
</main>
</body>
</html>
```